Drinks menu for our organic restaurant

We need a new menu design for our restaurant based in Glastonbury, UK. We are an organic, wholefood restaurant with an ethical sourcing policy, off...

Target Market(s)

Ladies that Lunch, foodies, people with an specific diet - health consious, vegan, organic, gluten-free.

Industry/Entity Type

Restaurant

Requirements
Must have
• The items on the menu may change from time to time so it must be in a format that we can edit. We will be re-printing the menus often on our inhouse colour printer.
Nice to have
• Our style is simple, rustic, and the restaurant is furnished in natural woods and earthy colours.
Should not have
• Nothing garish - we are a small independent restaurant and want to represent our individual and quirky style.

```html
<!DOCTYPE html>
<html lang="en">
<head>
<meta charset="utf-8">
<title>Tall Acorn – Drinks Menu</title>
<link href="https://fonts.googleapis.com/css2?family=Comfortaa:wght@300;400;700&family=Raleway:ital,wght@0,400;0,500;1,400&display=swap" rel="stylesheet">
<style>
:root{
  --backdrop:#cfcfcf;
  --cream:#fdf8e6;
  --olive:#6b6a3b;
  --lime:#a9b13b;
  --ink:#3d3c2c;
  --muted:#6d6b58;
  --alert:#c9452e;
}
*{box-sizing:border-box;margin:0;padding:0}
html,body{width:1200px;height:1000px;overflow:hidden}
body{background:var(--backdrop);position:relative;font-family:"Raleway",sans-serif;color:var(--ink)}
.page{position:absolute;background:var(--cream)}
.heading{font-family:"Comfortaa",sans-serif;color:var(--lime);text-align:center;line-height:1;white-space:nowrap}

/* wine list */
.wine-page{left:72px;top:148px;width:255px;height:660px}
.cover-panel{position:absolute;left:327px;top:148px;width:253px;height:660px;background:var(--olive)}
.wine-title{position:absolute;left:0;width:100%;top:22px;font-size:32px;font-weight:400}
.wine-note{position:absolute;left:0;width:100%;top:59px;font-size:7px;text-align:center;color:var(--muted)}
.measure-bar{position:absolute;left:0;width:255px;height:7px;background:var(--lime);display:grid;grid-template-columns:141px 27px 27px 27px 27px;font-size:5px;color:var(--cream);align-items:center}
.measure-bar span:first-child{visibility:hidden}
.cover-rule{position:absolute;left:327px;top:226px;width:253px;height:3px;background:var(--lime)}
.wine-section{position:absolute;left:13px;width:236px}
.wine-cat{font-size:12.5px;font-weight:500;letter-spacing:.3px;margin-bottom:1px}
.wine-row{display:grid;grid-template-columns:128px 27px 27px 27px 27px;margin-bottom:7px}
.wine-name{font-size:9px;line-height:10.5px}
.wine-desc{font-size:5px;line-height:6px;font-style:italic;color:var(--muted);margin-top:1px}
.price{font-size:6px;padding-top:20px;text-align:left}
.price.top{padding-top:12px}

/* cover */
.monkey-art{position:absolute;left:442px;top:222px;width:76px;height:100px;border-radius:36px 36px 28px 28px;background:linear-gradient(180deg,#a9b13b,#959c35)}
.cover-title{position:absolute;left:378px;top:340px;font-family:"Comfortaa",sans-serif;font-weight:300;font-size:34px;line-height:32px;color:var(--lime)}
.cover-title span{display:block}
.cover-title span+span{padding-left:42px}
.brand-box{position:absolute;left:380px;top:733px;width:147px;height:57px;background:var(--lime);display:flex;align-items:center;justify-content:center;gap:7px}
.brand-box i{width:9px;height:9px;border-radius:50%;background:var(--olive);display:block}
.brand-name{font-family:"Comfortaa",sans-serif;font-weight:400;font-size:19px;color:var(--olive)}

/* tea pages */
.tea-left{left:618px;top:148px;width:255px;height:660px}
.tea-right{left:873px;top:148px;width:255px;height:660px}
.tea-col{position:absolute;left:50px;width:170px}
.tea-heading{font-size:29px;font-weight:700;letter-spacing:-.3px}
.tea-price{font-size:8px;text-align:center;margin:4px 0 8px}
.tea-item{margin-bottom:8px}
.tea-name{font-size:8.6px;line-height:10px;display:flex;align-items:center;gap:3px}
.tea-desc{font-size:4.8px;line-height:5.8px;font-style:italic;color:var(--muted);width:160px}
.ico{width:9px;height:9px;flex:none}
.legend{position:absolute;left:38px;width:182px;top:576px;border-top:1px solid var(--muted);border-bottom:1px solid var(--muted);padding:6px 0 4px 16px;display:grid;grid-template-columns:84px 80px;row-gap:6px;font-size:5px;text-transform:uppercase}
.legend div{display:flex;align-items:center;gap:5px}
.legend .ico{width:11px;height:11px}
.folio{position:absolute;top:642px;font-size:7px;color:var(--muted)}
</style>
</head>
<body>

<!-- spread one: wine list and cover -->
<section class="page wine-page">
  <h1 class="heading wine-title">Wine List</h1>
  <p class="wine-note">all our wines are organic and suitable for vegans</p>
  <div class="measure-bar" style="top:76px"><span>.</span><span>125 ml</span><span>175 ml</span><span>250 ml</span><span>bottle</span></div>

  <div class="wine-section" style="top:88px">
    <h2 class="wine-cat">SPARKLING</h2>
    <div class="wine-row"><div><p class="wine-name">Vallorso Prosecco Spumante Treviso Extra Dry Italy</p><p class="wine-desc">Scent of white-fleshed fruits. Finely structured with biscuit and apple palate. Full of persistent bubbles.</p></div><span class="price top"></span><span class="price top"></span><span class="price top"></span><span class="price top">21</span></div>
  </div>

  <div class="wine-section" style="top:152px">
    <h2 class="wine-cat">WHITE</h2>
    <div class="wine-row"><div><p class="wine-name">Collina Pinot Grigio/ Catarratto, 2015 Italy</p><p class="wine-desc">Sicilian white with mineral freshness, peach and pear crisp finish.</p></div><span class="price top">4.75</span><span class="price top">5.25</span><span class="price top">6.25</span><span class="price top">18</span></div>
    <div class="wine-row"><div><p class="wine-name">White Rioja Alverde, 2015 Viña Sorel, Spain</p><p class="wine-desc">Strikingly fresh with a clean, citrus quality.</p></div><span class="price top">5.25</span><span class="price top">5.60</span><span class="price top">6.60</span><span class="price top">19</span></div>
    <div class="wine-row"><div><p class="wine-name">Tierra Clara Sauvignon Blanc, 2015 Los Robles, Chile</p><p class="wine-desc">Fresh, delicate and pure, a natural expression of its origin. Certified carbon neutral and fair trade.</p></div><span class="price top">5.40</span><span class="price top">5.75</span><span class="price top">6.75</span><span class="price top">19.50</span></div>
    <div class="wine-row"><div><p class="wine-name">Chablis, Domaine Marcelin, Burgundy, France</p><p class="wine-desc">Well-defined, crisp citrus fruits and the minerally qualities that you would expect from the region.</p></div><span class="price"></span><span class="price"></span><span class="price"></span><span class="price top">23</span></div>
  </div>

  <div class="wine-section" style="top:324px">
    <h2 class="wine-cat">ROSE'</h2>
    <div class="wine-row"><div><p class="wine-name">Domaine de Lisle, Languedoc-Roussillion.</p><p class="wine-desc">The Merlot, Cabernet Sauvignon and Cinsault grapes ripen fully in the southern French sun, producing robust, juicy flavours.</p></div><span class="price top">4.75</span><span class="price top">5.25</span><span class="price top">6.25</span><span class="price top">18</span></div>
  </div>

  <div class="wine-section" style="top:387px">
    <h2 class="wine-cat">REDS</h2>
    <div class="wine-row"><div><p class="wine-name">Nero d'Avola, 2015 Monteverde Italy</p><p class="wine-desc">Nero d'Avola is a hearty and warm grape, soft and approachable with a black-fruited character.</p></div><span class="price top">4.75</span><span class="price top">5.25</span><span class="price top">6.25</span><span class="price top">18</span></div>
    <div class="wine-row"><div><p class="wine-name">Petit Sauló Cabernet/ Garnacha/Tempranillo, 2015 Sauló i Mas Spain</p><p class="wine-desc">Fantastic blend, nose wild strawberry, a mouth full of black fruits, serious weight and black pepper spice.</p></div><span class="price">5.25</span><span class="price">5.60</span><span class="price">6.60</span><span class="price">19</span></div>
    <div class="wine-row"><div><p class="wine-name">Tupungato Malbec, 2015 Domaine Arnaud, Argentina</p><p class="wine-desc">Subtle vanilla and chocolate notes from the oak and fantastic black plum and blackberry fruits.</p></div><span class="price top">5.60</span><span class="price top">6.20</span><span class="price top">7.20</span><span class="price top">23</span></div>
    <div class="wine-row"><div><p class="wine-name">Pinot Noir, Domaine de Lisle Languedoc-Roussillion</p><p class="wine-desc">This lightly-herbal southern French Pinot Noir has crunchy summer berry fruits and a good, long length of flavour in the palate.</p></div><span class="price"></span><span class="price"></span><span class="price"></span><span class="price top">24</span></div>
  </div>

  <div class="measure-bar" style="top:596px"><span>.</span><span>125 ml</span><span>175 ml</span><span>250 ml</span><span>37.5 ml</span></div>
  <div class="wine-section" style="top:609px">
    <div class="wine-row"><div><h2 class="wine-cat" style="margin:0">DESSERT</h2><p class="wine-name">Quiet Meadow Muscat</p><p class="wine-desc">A natural sweet wine produces from Muscat grapes dried on rooibos and straw. Scents and flavours of apricot and honey.</p></div><span class="price">5</span><span class="price">5.30</span><span class="price">6.60</span><span class="price">18.50</span></div>
  </div>
</section>

<section class="cover-panel" aria-label="Menu cover"></section>
<div class="cover-rule"></div>
<div class="monkey-art" role="img" aria-label="Illustration of a monkey hanging by one arm from the rule"></div>
<p class="cover-title"><span>drinks</span><span>menu</span></p>
<div class="brand-box"><i></i><span class="brand-name">Tall Acorn</span></div>

<!-- spread two: teas -->
<section class="page tea-left">
  <div class="tea-col" style="top:12px">
    <h2 class="heading tea-heading">Black Tea</h2>
    <p class="tea-price">£2.50</p>
    <div class="tea-item"><p class="tea-name">Assam Rivermist (India)</p><p class="tea-desc">Broken and then granulated leaves provides a dark mahogany infusion with a rich, malty and exquisitely smooth flavour. The ideal breakfast tea.</p></div>
    <div class="tea-item"><p class="tea-name">English Breakfast <svg class="ico" viewBox="0 0 10 10"><circle cx="5" cy="5" r="4.4" fill="none" stroke="var(--lime)" stroke-width=".8"/><path d="M3.3 6.8C3.3 4.5 5 3.2 7 3 6.9 5.2 5.5 6.8 3.3 6.8z" fill="var(--lime)"/></svg></p><p class="tea-desc">A blend of large leaf Ceylon and Assam teas. Gives a golden brown infusion with a rich aroma and flavour. Ideal with a dash of milk.</p></div>
    <div class="tea-item"><p class="tea-name">Darjeeling First Flush (India)</p><p class="tea-desc">A blend of early spring picked teas from various gardens in Darjeeling. Contains a high amount of golden tips, which gives a golden infusion with a well-balanced flavour.</p></div>
    <div class="tea-item"><p class="tea-name">Golden Nepal First Flush</p><p class="tea-desc">A high grown tea produced in the Himalayan mountains. This tea is very similar to Darjeeling tea but it gives a much stronger infusion.</p></div>
    <div class="tea-item"><p class="tea-name">Ceylon OP Dimbula Highgrove<br>(Sri Lanka)</p><p class="tea-desc">This delicious tea is grown 1400m above sea level. The infusion is brown in colour with a sweet, smooth and well-balanced flavour.</p></div>
    <div class="tea-item"><p class="tea-name">Lapsang Souchong (China)</p><p class="tea-desc">A speciality tea of the Fujian province in China. In the final stage of production the tea is hung in baskets over smoking pine wood fires to dry. Intense smokey aroma and taste.</p></div>
    <div class="tea-item"><p class="tea-name">Earl Grey <svg class="ico" viewBox="0 0 10 10"><circle cx="5" cy="5" r="4.4" fill="none" stroke="var(--lime)" stroke-width=".8"/><ellipse cx="5" cy="5.2" rx="1.6" ry="2.2" fill="var(--lime)"/></svg></p><p class="tea-desc">Ceylon black tea, bergamot aroma.<br>May contain traces of nuts.</p></div>
    <div class="tea-item"><p class="tea-name">Earl Grey Imperial <svg class="ico" viewBox="0 0 10 10"><circle cx="5" cy="5" r="4.4" fill="none" stroke="var(--lime)" stroke-width=".8"/><ellipse cx="5" cy="5.2" rx="1.6" ry="2.2" fill="var(--lime)"/></svg></p><p class="tea-desc">Ceylon black tea, superb quality Italian bergamot, jasmine flowers. May contain traces of nuts.</p></div>
  </div>

  <div class="tea-col" style="top:372px">
    <h2 class="heading tea-heading" style="font-size:33px;line-height:34px">Specialty<br>Teas</h2>
    <p class="tea-price">£2.90</p>
    <div class="tea-item"><p class="tea-name">Pu-Erh Sweet Chai <svg class="ico" viewBox="0 0 10 10"><circle cx="5" cy="5" r="4.4" fill="none" stroke="var(--lime)" stroke-width=".8"/><ellipse cx="5" cy="5.2" rx="1.6" ry="2.2" fill="var(--lime)"/></svg></p><p class="tea-desc">Ingredients: Pu-Erh tea, cinnamon, liquorice, aroma, ginger, sandal wood, cloves, flowers of thistle.<br>May contain traces of nuts.</p></div>
    <div class="tea-item"><p class="tea-name">Oolong Tea – Ti Kuan Yin</p><p class="tea-desc">This is one of the most popular of the Chinese oolongs. It was named by a tea growers after the statue of the "Goddess of Mercy". The infusion is sweet with floral notes.</p></div>
    <div class="tea-item"><p class="tea-name">Organic Ayurvedic Tea <svg class="ico" viewBox="0 0 10 10"><path d="M1.5 8.5C1.5 4.5 4.5 1.8 8.8 1.5 8.5 6 5.8 8.5 1.5 8.5z" fill="var(--lime)"/></svg></p><p class="tea-desc">Organic cinnamon, organic ginger, organic cloves, organic black peppercorns.</p></div>
  </div>

  <div class="legend">
    <div><svg class="ico" viewBox="0 0 10 10"><path d="M1.5 8.5C1.5 4.5 4.5 1.8 8.8 1.5 8.5 6 5.8 8.5 1.5 8.5z" fill="var(--lime)"/></svg>Organic</div>
    <div><svg class="ico" viewBox="0 0 10 10"><circle cx="5" cy="5" r="4.4" fill="none" stroke="var(--lime)" stroke-width=".8"/><path d="M3.3 6.8C3.3 4.5 5 3.2 7 3 6.9 5.2 5.5 6.8 3.3 6.8z" fill="var(--lime)"/></svg>Contain lactose</div>
    <div><svg class="ico" viewBox="0 0 10 10"><circle cx="5" cy="5" r="4.4" fill="none" stroke="var(--lime)" stroke-width=".8"/><ellipse cx="5" cy="5.2" rx="1.6" ry="2.2" fill="var(--lime)"/></svg>Contain nuts</div>
    <div><svg class="ico" viewBox="0 0 10 10"><circle cx="5" cy="5" r="4.4" fill="none" stroke="var(--alert)" stroke-width=".9"/><line x1="2" y1="8" x2="8" y2="2" stroke="var(--alert)" stroke-width=".9"/><rect x="3.4" y="4" width="3" height="2.6" fill="var(--alert)"/></svg>Caffeine free</div>
  </div>
  <p class="folio" style="left:10px">01</p>
</section>

<section class="page tea-right">
  <div class="tea-col" style="top:12px">
    <h2 class="heading tea-heading">Green Tea</h2>
    <div style="height:14px"></div>
    <div class="tea-item"><p class="tea-name">China Gunpowder</p><p class="tea-desc">Large leaves are rolled into little pellets reminiscent of gunpowder. It gives a yellow infusion with a rich taste.</p></div>
    <div class="tea-item"><p class="tea-name">China Sencha</p><p class="tea-desc">A Japanese style green tea grown in China provides a bright yellow infusion with a grassy and subtle nutty flavour.</p></div>
    <div class="tea-item"><p class="tea-name">China Jasmine with Flowers</p><p class="tea-desc">Contains dried Jasmine flowers Lemon and Ginger. Pieces of ginger, lemon grass, pieces of lemon.</p></div>
    <div class="tea-item"><p class="tea-name">Little Lotus <svg class="ico" viewBox="0 0 10 10"><circle cx="5" cy="5" r="4.4" fill="none" stroke="var(--lime)" stroke-width=".8"/><ellipse cx="5" cy="5.2" rx="1.6" ry="2.2" fill="var(--lime)"/></svg></p><p class="tea-desc">Green tea China Sencha, liquorice, sandalwood, red peppercorns, aroma, Roman camomile, pineapple (sugar, citric acid). May contain traces of nuts.</p></div>
    <div class="tea-item"><p class="tea-name">Bancha Arashyama</p><p class="tea-desc">Japanese green tea, low in caffeine.</p></div>
  </div>

  <div class="tea-col" style="top:214px">
    <h2 class="heading tea-heading" style="font-size:25px">Single Herbs</h2>
    <p class="tea-price">£2.50</p>
    <div class="tea-item"><p class="tea-name">Chamomile <svg class="ico" viewBox="0 0 10 10"><circle cx="5" cy="5" r="4.4" fill="none" stroke="var(--alert)" stroke-width=".9"/><line x1="2" y1="8" x2="8" y2="2" stroke="var(--alert)" stroke-width=".9"/><rect x="3.4" y="4" width="3" height="2.6" fill="var(--alert)"/></svg></p><p class="tea-desc">Helps boost the immune system and fight infections associated with colds. It is mildly sedative and has calming effect. Caffeine free.</p></div>
    <div class="tea-item"><p class="tea-name">Organic Roibos <svg class="ico" viewBox="0 0 10 10"><circle cx="5" cy="5" r="4.4" fill="none" stroke="var(--alert)" stroke-width=".9"/><line x1="2" y1="8" x2="8" y2="2" stroke="var(--alert)" stroke-width=".9"/><rect x="3.4" y="4" width="3" height="2.6" fill="var(--alert)"/></svg><svg class="ico" viewBox="0 0 10 10"><path d="M1.5 8.5C1.5 4.5 4.5 1.8 8.8 1.5 8.5 6 5.8 8.5 1.5 8.5z" fill="var(--lime)"/></svg></p><p class="tea-desc">Naturally caffeine free, rich in antioxidants, minerals and vitamin C. It has soothing effect on the nervous system and anti-spasmodic properties.</p></div>
    <div class="tea-item"><p class="tea-name">Triple Mint</p><p class="tea-desc">Ingredients: Spearmint, Peppermint Willamette, Large leaf Mint-Mentha Piperitae.</p></div>
    <div class="tea-item"><p class="tea-name">Nettle</p><p class="tea-desc">Helps stimulate blood circulation and metabolism. It contains antioxidants and helps lower blood pressure.</p></div>
  </div>

  <div class="tea-col" style="top:398px">
    <h2 class="heading tea-heading" style="font-size:23px;line-height:24px">Herbal &amp; Fruit<br>Mixes</h2>
    <p class="tea-price">£2.70</p>
    <div class="tea-item"><p class="tea-name">Tea for Good Digestion</p><p class="tea-desc">Peppermint leaves, Camomile flowers, anise, fennel seeds, caraway seeds, mallow flowers, marigolds.</p></div>
    <div class="tea-item"><p class="tea-name">Good Mood &amp; Memory</p><p class="tea-desc">Lemon balm, lemon grass, oregano, rosemary, ginseng root, schizandra berries, lavender, mullein flowers.</p></div>
    <div class="tea-item"><p class="tea-name">Herbal Detox Tisane</p><p class="tea-desc">Nettle leaves, organic rooibos, camomile, nana mint, fennel seeds, ginger and liquorice, peppermint, sage.</p></div>
    <div class="tea-item"><p class="tea-name">Orchard Garden <svg class="ico" viewBox="0 0 10 10"><circle cx="5" cy="5" r="4.4" fill="none" stroke="var(--lime)" stroke-width=".8"/><ellipse cx="5" cy="5.2" rx="1.6" ry="2.2" fill="var(--lime)"/></svg></p><p class="tea-desc">Elderberries, blackberries, raspberries, strawberries, chokeberries, redcurrant, beetroot, apple, hibiscus, blackberry leaves. May contain traces of nuts.</p></div>
    <div class="tea-item"><p class="tea-name">Pumpkin and Turmeric <svg class="ico" viewBox="0 0 10 10"><circle cx="5" cy="5" r="4.4" fill="none" stroke="var(--lime)" stroke-width=".8"/><ellipse cx="5" cy="5.2" rx="1.6" ry="2.2" fill="var(--lime)"/></svg></p><p class="tea-desc">Apple, pumpkin, orange peel, carrot, turmeric, cinnamon, cocoa-kernels, marigolds, cloves. May contain traces of nuts.</p></div>
    <div class="tea-item"><p class="tea-name">Roibos Savanna <svg class="ico" viewBox="0 0 10 10"><circle cx="5" cy="5" r="4.4" fill="none" stroke="var(--lime)" stroke-width=".8"/><ellipse cx="5" cy="5.2" rx="1.6" ry="2.2" fill="var(--lime)"/></svg></p><p class="tea-desc">Organic rooibos, lemon grass, orange peel, aroma, marigold, thistle flowers. May contain traces of nuts.</p></div>
  </div>
  <p class="folio" style="right:12px">02</p>
</section>

</body>
</html>
```